Webdesign/Updates

We would like a landing page for an online course for our educators. So a website with about 3 to 5 pages - Home, About US, Online course, blog, and Contact us. We have a wordpress site up using a template, but we are looking for something that connects more with our new logo.

Target Market(s)

Educators, workshop trainers/instructors, colleges, community schools, educational institutions, global organizations

Industry/Entity Type

Education

Contact Information for Business Card

Use the words below as place holders for the front:
Name
Title
Address line 1
Address line 2
Email
Phone
Website URL

--the back
Logo
1 short question, use "What do you 1234 about your program?"

Number of Pages Required

4 page

Requirements
Must have
• Home page
• Course Page
• Blog
• right side bar with social media content and invitation to subscribe to newsletter
• see logo colors in document
Nice to have
• Newsletter Page with graphic that can be on this page or page can be sent as a pdf via email or in an email.
Should not have
• Be better than attached description
• clean simple look but stylish

```html
<!DOCTYPE html>
<html lang="en">
<head>
<meta charset="utf-8">
<title>Brightpath Learning – Online Course Design</title>
<link href="https://fonts.googleapis.com/css2?family=Nunito:wght@400;600;700;800&display=swap" rel="stylesheet">
<style>
:root{
  --accent:#f04a23;
  --blue:#1e8fd8;
  --blue-deep:#1679c0;
  --ink:#141414;
  --text:#4a4a4a;
  --mist:#e3eef2;
  --mist-deep:#cfe2e9;
  --footer:#1d1d1d;
  --footer-text:#c9c9c9;
  --white:#ffffff;
  --icon-ring:#6bb4d6;
  --icon-ring-alt:#8cc63f;
}
*{box-sizing:border-box;margin:0;padding:0}
html,body{width:1200px;height:4215px;overflow:hidden}
body{font-family:"Nunito",sans-serif;color:var(--text);background:var(--white);position:relative}
section,header,footer{position:absolute;left:0;width:1200px}
.abs{position:absolute}
.btn{display:inline-block;background:var(--accent);color:var(--white);font-weight:700;font-size:14px;border-radius:20px;padding:0 22px;line-height:36px;text-transform:uppercase;letter-spacing:.5px}

/* header */
.site-header{top:0;height:90px;background:var(--white)}
.brand{left:132px;top:26px;display:flex;align-items:center;gap:12px}
.brand-dot{width:30px;height:30px;border-radius:50%;background:var(--accent)}
.brand-name{font-size:30px;font-weight:800;color:var(--blue)}
.main-nav{right:132px;top:36px;display:flex;gap:26px;font-size:16px;font-weight:700;color:var(--ink);text-transform:uppercase}

/* hero */
.hero{top:90px;height:607px;overflow:hidden}
.hero-photo{position:absolute;inset:0;background:linear-gradient(100deg,#c9b7a2 0%,#8d7564 35%,#4d4a4e 65%,#2b2c33 100%)}
.hero-shade{position:absolute;inset:0}
.hero-title{left:725px;top:218px;width:420px;font-size:35px;font-weight:700;color:var(--white);letter-spacing:.3px;white-space:nowrap}
.hero-copy{left:725px;top:272px;width:400px;font-size:15.5px;line-height:28px;color:var(--white);text-align:center}
.hero-btn{left:853px;top:381px}
.hero-dots{left:855px;top:455px;display:flex;gap:8px}
.hero-dots span{width:12px;height:12px;border:2px solid var(--white);border-radius:50%}
.hero-dots span:first-child{background:var(--accent);border-color:var(--accent)}

/* intro */
.intro{top:697px;height:582px}
.section-title{width:100%;text-align:center;font-size:33px;font-weight:800;color:var(--ink);text-transform:uppercase}
.section-title em{font-style:normal;color:var(--accent)}
.section-sub{width:100%;text-align:center;font-size:20px;color:var(--ink)}
.intro .section-title{top:88px}
.intro .section-sub{top:137px}
.intro-copy{left:132px;top:265px;width:492px;font-size:14px;line-height:24px;color:var(--text)}
.intro-btn{left:132px;top:463px}
.video-frame{left:660px;top:230px;width:422px;height:287px}
.video-photo{position:absolute;left:0;top:0;width:422px;height:287px;background:linear-gradient(135deg,#6b5b4b,#3b3530 60%,#2a2a2a)}

/* features */
.features{top:1279px;height:740px}
.features .section-title{top:186px;font-size:30px}
.features .section-sub{top:236px}
.feature{width:215px}
.feature h3{font-size:18px;font-weight:700;color:var(--ink);margin-bottom:8px}
.feature p{font-size:13px;line-height:22px}
.feature.left{text-align:right}
.feature-icon{width:82px;height:82px}
.course-graphic{left:458px;top:342px;width:290px;height:290px;border-radius:50%;background:radial-gradient(circle,#f4f4f4 0 45%,#e9a23b 46% 60%,#2e6fb7 61% 80%,#d8342c 81%)}

/* objectives */
.objectives{top:1981px;height:736px;background:var(--blue)}
.objectives .section-title{top:160px;color:var(--white);font-size:33px}
.objectives .section-sub{top:214px;color:#dcefff;font-size:19px}
.presenter{left:0;top:295px;width:323px;height:441px;background:linear-gradient(180deg,#e2c7a8 0%,#b8957a 35%,#2b3440 60%,#1f2530 100%)}
.goal-card{top:323px;width:214px;height:268px;background:var(--white);border-radius:12px;text-align:center;padding-top:26px;box-shadow:0 6px 18px rgba(0,0,0,.18)}
.goal-art{width:110px;height:100px;margin:0 auto 16px;border-radius:10px;background:linear-gradient(135deg,#f6a33a,#2f76c3)}
.goal-card h3{font-size:18px;font-weight:700;color:var(--ink);text-transform:uppercase;margin-bottom:10px}
.goal-card p{font-size:13px;line-height:21px;padding:0 20px}

/* testimonials */
.testimonials{top:2717px;height:590px;background:#fafafa}
.testimonials .section-title{top:92px}
.title-rule{left:570px;top:148px;width:60px;height:3px;background:var(--blue)}
.quote-card{top:216px;width:407px;height:206px;background:var(--white);box-shadow:0 4px 16px rgba(0,0,0,.15);padding:26px 30px;font-size:13px;line-height:22px}
.quote-by{position:absolute;bottom:24px;color:var(--blue);font-size:13px;line-height:20px}
.quote-mark{position:absolute;bottom:18px;font-size:64px;line-height:40px;color:#8a8a8a;font-weight:800}
.avatar{width:112px;height:112px;border-radius:50%;border:5px solid var(--white);background:linear-gradient(180deg,#cfd3d8,#7c8590);box-shadow:0 3px 10px rgba(0,0,0,.2)}

/* newsletter */
.newsletter{top:3307px;height:470px;overflow:hidden}
.newsletter-photo{position:absolute;inset:0;background:linear-gradient(100deg,#d6d8da 0%,#b8bcc0 45%,#8f8a86 70%,#5a4f48 100%)}
.newsletter-box{left:303px;top:116px;width:591px;height:216px;background:rgba(30,143,216,.92);border-radius:4px;text-align:center}
.newsletter-box h2{position:absolute;top:86px;width:100%;font-size:32px;font-weight:800;color:var(--white);text-transform:uppercase}
.newsletter-form{position:absolute;left:38px;top:152px;width:515px;height:48px;display:flex;border-radius:24px;overflow:hidden}
.newsletter-form .field{flex:1;background:var(--white);text-align:left;padding-left:24px;line-height:48px;font-size:13px;color:#9a9a9a}
.newsletter-form .send{width:124px;background:var(--accent);color:var(--white);line-height:48px;font-weight:700;font-size:14px}

/* footer */
.site-footer{top:3766px;height:449px;background:var(--footer);color:var(--footer-text)}
.footer-col h4{font-size:20px;font-weight:800;color:var(--white);text-transform:uppercase;margin-bottom:24px}
.link-list{list-style:none;font-size:14px;line-height:24px}
.link-list li::before{content:"›";margin-right:12px}
.contact-list{list-style:none;font-size:14px;line-height:20px}
.contact-list li{display:flex;gap:12px;margin-bottom:12px}
.contact-list svg{flex:none;margin-top:3px}
.quote-intro{font-size:13.5px;line-height:20px;margin-bottom:18px}
.form-grid{display:grid;grid-template-columns:210px 210px;gap:10px 16px}
.form-field{height:40px;border:1px solid #5a5a5a;font-size:12px;line-height:40px;padding-left:12px;color:#9a9a9a}
.form-submit{height:40px;background:var(--accent);color:var(--white);text-align:center;line-height:40px;font-weight:800;font-size:16px;text-transform:uppercase}
.social{left:540px;top:357px;display:flex;gap:6px}
.social span{width:20px;height:20px;border:1.5px solid #bbb;border-radius:50%}
.copyright{top:395px;width:100%;text-align:center;font-size:13px}
</style>
</head>
<body>

<header class="site-header">
  <div class="brand abs"><span class="brand-dot"></span><span class="brand-name">Brightpath Learning</span></div>
  <nav class="main-nav abs"><span>Home</span><span>Course</span><span>Blog</span><span>Consulting</span><span>About Me</span><span>Contact Us</span></nav>
</header>

<section class="hero">
  <div class="hero-photo" role="img" aria-label="Photo of educators working together at a laptop"></div>
  <svg class="hero-shade" width="1200" height="607" viewBox="0 0 1200 607">
    <polygon points="730,0 1200,0 1200,607 560,607 660,300" fill="#1b1b20" opacity=".6"/>
    <polyline points="730,0 660,300 560,607" fill="none" stroke="#ffffff" stroke-width="3" opacity=".8"/>
  </svg>
  <h1 class="hero-title abs">BRIGHTPATH LEARNING</h1>
  <p class="hero-copy abs">Sed ut perspiciatis unde omnis iste natus error sit voluptatem accusantium doloremque laudantium, totam rem aperiam, eaque ipsa quae</p>
  <span class="btn hero-btn abs">Get Started</span>
  <div class="hero-dots abs"><span></span><span></span><span></span><span></span><span></span><span></span></div>
</section>

<section class="intro">
  <h2 class="section-title abs">The Ultimate <em>Course</em> Design <em>Program</em></h2>
  <p class="section-sub abs">A practical, Comprehensive Approach Gets you Ahead</p>
  <p class="intro-copy abs">Sed ut perspiciatis unde omnis iste natus error sit voluptatem accusantium doloremque laudantium, totam rem aperiam, eaque ipsa quae ab illo inventore veritatis et quasi architecto beatae vitae dicta sunt explicabo. Nemo enim ipsam voluptatem quia voluptas sit aspernatur aut odit aut fugit, sed quia ntur magni dolores eos qui ratione voluptatem sequi nesciunt. Neque porro Sed ut perspiciatis unde omnis iste natus</p>
  <span class="btn intro-btn abs">Get Started</span>
  <div class="video-frame abs">
    <div class="video-photo" role="img" aria-label="Video still of a student studying with headphones in a library"></div>
    <svg class="abs" style="left:-10px;top:-10px" width="442" height="307" viewBox="0 0 442 307">
      <g fill="none" stroke="#333" stroke-width="2">
        <path d="M1 30V1H30"/><path d="M412 1H441V30"/><path d="M1 277V306H30"/><path d="M412 306H441V277"/>
      </g>
      <circle cx="221" cy="153" r="32" fill="#ffffff" opacity=".9"/>
      <polygon points="212,138 212,168 236,153" fill="#222"/>
    </svg>
  </div>
</section>

<section class="features">
  <svg class="abs" style="left:0;top:0" width="1200" height="740" viewBox="0 0 1200 740">
    <path d="M0 40 C200 -10 380 90 600 60 C820 30 1000 110 1200 70 V740 H0Z" fill="var(--mist-deep)"/>
    <path d="M0 80 C220 30 420 130 640 95 C860 60 1020 140 1200 110 V740 H0Z" fill="var(--mist)"/>
  </svg>
  <h2 class="section-title abs">The Ultimate Course Design Program Features</h2>
  <p class="section-sub abs">A collaborative Approach to Creating Accreditable Online Courses</p>

  <div class="feature left abs" style="left:102px;top:345px">
    <h3>Effective Lessons</h3>
    <p>Sed ut perspiciatis unde omnis iste natus error sit voluptatem cusantium doloremque ntium, totam rem aperiam</p>
  </div>
  <svg class="feature-icon abs" style="left:333px;top:355px" viewBox="0 0 82 82"><circle cx="41" cy="41" r="38" fill="#fff" stroke="var(--icon-ring-alt)" stroke-width="3"/><rect x="25" y="28" width="32" height="22" rx="2" fill="none" stroke="var(--blue)" stroke-width="3"/><path d="M35 56H47M41 50V56" stroke="var(--blue)" stroke-width="3"/></svg>

  <div class="feature left abs" style="left:102px;top:527px">
    <h3>Quality Videos</h3>
    <p>Sed ut perspiciatis unde omnis iste natus error sit voluptatem cusantium doloremque ntium, totam rem aperiam</p>
  </div>
  <svg class="feature-icon abs" style="left:333px;top:535px" viewBox="0 0 82 82"><circle cx="41" cy="41" r="38" fill="#fff" stroke="var(--icon-ring-alt)" stroke-width="3"/><rect x="28" y="25" width="26" height="32" rx="2" fill="none" stroke="var(--blue)" stroke-width="3"/><polygon points="37,34 37,48 47,41" fill="var(--blue)"/></svg>

  <div class="course-graphic abs" role="img" aria-label="Illustration of an open book on a laptop inside a coloured ring"></div>

  <svg class="feature-icon abs" style="left:779px;top:340px" viewBox="0 0 82 82"><circle cx="41" cy="41" r="38" fill="#fff" stroke="var(--icon-ring)" stroke-width="3"/><rect x="27" y="27" width="28" height="28" rx="2" fill="none" stroke="var(--blue)" stroke-width="3"/><path d="M33 41L39 47L50 35" fill="none" stroke="var(--blue)" stroke-width="3"/></svg>
  <div class="feature abs" style="left:880px;top:335px">
    <h3>Awesome Quizzes</h3>
    <p>Sed ut perspiciatis unde omnis iste natus error sit voluptatem cusantium doloremque ntium, totam rem aperiam</p>
  </div>

  <svg class="feature-icon abs" style="left:799px;top:525px" viewBox="0 0 82 82"><circle cx="41" cy="41" r="38" fill="#fff" stroke="var(--icon-ring-alt)" stroke-width="3"/><path d="M41 24V46M32 38L41 47L50 38" fill="none" stroke="var(--blue)" stroke-width="3"/><path d="M27 50V57H55V50" fill="none" stroke="var(--blue)" stroke-width="3"/></svg>
  <div class="feature abs" style="left:900px;top:527px">
    <h3>Hosted Content</h3>
    <p>Sed ut perspiciatis unde omnis iste natus error sit voluptatem cusantium doloremque ntium, totam rem aperiam</p>
  </div>
</section>

<section class="objectives">
  <svg class="abs" style="left:0;top:-40px" width="1200" height="80" viewBox="0 0 1200 80"><path d="M0 40 C300 80 600 20 1200 40 V80 H0Z" fill="var(--blue)"/></svg>
  <h2 class="section-title abs">Learning Objectives</h2>
  <p class="section-sub abs">So many academic goals that we expect you &nbsp;to achieve</p>
  <div class="presenter abs" role="img" aria-label="Photo of a smiling teacher in a dark blazer pointing to the cards"></div>
  <article class="goal-card abs" style="left:360px">
    <div class="goal-art" role="img" aria-label="Illustration of a person beside a skills chart"></div>
    <h3>Skills</h3>
    <p>Sed ut perspiciatis unde omnis iste natus error sit voluptatem accusantium doloremque</p>
  </article>
  <article class="goal-card abs" style="left:607px">
    <div class="goal-art" role="img" aria-label="Illustration of a learner at a computer"></div>
    <h3>Self Learning</h3>
    <p>Sed ut perspiciatis unde omnis iste natus error sit voluptatem accusantium doloremque</p>
  </article>
  <article class="goal-card abs" style="left:854px">
    <div class="goal-art" role="img" aria-label="Illustration of books beside a globe"></div>
    <h3>Knowledge</h3>
    <p>Sed ut perspiciatis unde omnis iste natus error sit voluptatem accusantium doloremque</p>
  </article>
</section>

<section class="testimonials">
  <h2 class="section-title abs">Testimonials</h2>
  <div class="title-rule abs"></div>
  <blockquote class="quote-card abs" style="left:155px">
    Sed ut perspiciatis unde omnis iste natus error sit voluptatem accusantium doloremque laudantium, totam rem aperiam, eaque ipsa quae ab illo inventore veritatis et quasi architecto beatae vitae dicta sunt explicabo.
    <span class="quote-by" style="left:30px">John Doe -<br>Brightpath Learning</span>
    <span class="quote-mark" style="left:192px">”</span>
  </blockquote>
  <div class="avatar abs" style="left:463px;top:340px" role="img" aria-label="Portrait photo of the reviewer"></div>
  <blockquote class="quote-card abs" style="left:635px;text-align:right">
    Sed ut perspiciatis unde omnis iste natus error sit voluptatem accusantium doloremque laudantium, totam rem aperiam, eaque ipsa quae ab illo inventore veritatis et quasi architecto beatae vitae dicta sunt explicabo.
    <span class="quote-by" style="right:30px">John Doe -<br>Brightpath Learning</span>
    <span class="quote-mark" style="right:192px">“</span>
  </blockquote>
  <div class="avatar abs" style="left:607px;top:340px" role="img" aria-label="Portrait photo of the reviewer"></div>
</section>

<section class="newsletter">
  <div class="newsletter-photo" role="img" aria-label="Photo of a student in glasses reading at a desk"></div>
  <div class="newsletter-box abs">
    <svg class="abs" style="left:270px;top:28px" width="52" height="46" viewBox="0 0 52 46"><path d="M3 22L49 3L40 42L26 32L20 43L19 29Z" fill="none" stroke="#fff" stroke-width="3" stroke-linejoin="round"/><path d="M19 29L49 3" stroke="#fff" stroke-width="3"/></svg>
    <h2>Newsletter Sign Up</h2>
    <div class="newsletter-form"><span class="field">Enter your email address</span><span class="send">SUBSCRIBE</span></div>
  </div>
  <svg class="abs" style="left:0;top:410px" width="1200" height="60" viewBox="0 0 1200 60"><path d="M0 60 C300 20 800 10 1200 20 V60Z" fill="var(--footer)"/><path d="M0 58 C300 18 800 8 1200 18" fill="none" stroke="var(--accent)" stroke-width="5"/></svg>
</section>

<footer class="site-footer">
  <div class="footer-col abs" style="left:132px;top:58px">
    <h4>Quick Links</h4>
    <ul class="link-list"><li>Home</li><li>Course</li><li>Blog</li><li>Consulting</li><li>About Me</li><li>Contact</li></ul>
  </div>
  <div class="footer-col abs" style="left:332px;top:58px;width:260px">
    <h4>Contact Us</h4>
    <ul class="contact-list">
      <li><svg width="12" height="16" viewBox="0 0 12 16"><path d="M6 0C2.7 0 0 2.6 0 5.9 0 10 6 16 6 16S12 10 12 5.9C12 2.6 9.3 0 6 0ZM6 8A2 2 0 1 1 6 4 2 2 0 0 1 6 8Z" fill="#ddd"/></svg><span>Brightpath Learning<br>Via Lungarno 14 - 53100<br>Siena - Italy</span></li>
      <li><svg width="14" height="14" viewBox="0 0 14 14"><path d="M3 0L5.5 3.5 4 5.5C5 7.5 6.5 9 8.5 10L10.5 8.5 14 11 12 14C5.5 13.5 0.5 8.5 0 2Z" fill="#ddd"/></svg><span>Phone 800-555-0142<br>Fax 0577 550199</span></li>
      <li><svg width="14" height="11" viewBox="0 0 14 11"><rect x=".5" y=".5" width="13" height="10" fill="none" stroke="#ddd"/><path d="M.5 .5L7 6 13.5 .5" fill="none" stroke="#ddd"/></svg><span>Email: info@brightpathlearning.com</span></li>
    </ul>
  </div>
  <div class="footer-col abs" style="left:632px;top:58px;width:440px">
    <h4>Get A Quote</h4>
    <p class="quote-intro">Lorem ipsum dolor sit amet, consectetur adipiscing elit, sed do eiusmod tempor incididunt ut labore et dolore magna aliqua</p>
    <div class="form-grid">
      <span class="form-field">Name</span><span class="form-field">E - Mail</span>
      <span class="form-field">Phone No</span><span class="form-submit">Submit</span>
    </div>
  </div>
  <div class="social abs"><span></span><span></span><span></span><span></span></div>
  <p class="copyright abs">© 2018 Brightpath Learning. All Rights Reserved.</p>
</footer>

</body>
</html>
```